Help develop the "Breezy Brew" Logo & Can Design for new beer!

We're a new beer being produced in the Caribbean. Thus looking for a beer logo design that
1) capitalizes on the word "Breezy" for further beer lines that spin off of this first one. EXAMPLES OF OTHER BEER NAMES TO BE PRODUCED THAT HAVE TO HAVE TIE IN TO ORIGINAL DESIGN: "One Breezy Brew", "Sunny Pelican Wobble Brew" "Ramblefoot Breezy Brew" "Wharrya doin' Breezy Brew" "Bout now for Breezy Brew", "Tamarna Breezy Brew" etc etc etc,

2) has unique visual impact,
3) Logo has to be usable across variety of mediums,
4) 4 color maximum,
5) Island art feel,
6) Breezy Brew needs to convey a since of "lightness and slight tongue-in-cheek or off beat humor"...but not overwhelming,
7) Each subsequent label names (see above) needs to be distinctly color coded, but connects to the overarching theme of the brand with distinctive interpretations of each beer’s name.
8) Needs to be BOLD in statement and color.

You can get inspiration from some of these logo's. Follow this link: http://www.quorvelstudio.com/vintage-logos/
or http://www.tindralcrate.com/2014/12/30-beers-for-30-years-2001-to-2006.html

Also see attached files for inspiration!!!

Reason: We've extended the deadline for this project! Thus submit any new designs sooner than later. Thanks!

Target Market(s)

Male: Wear jeans & baseball cap, Played H.S. sports, Hunts/fish/golfDrive a truck or SUV, Work a blue collar job, Like working in the garage or on the landLike football/basketball/baseball, Are married high school sweetheart and have childrenAre from southern states...or wished they were, Chews tobacco or smokeDrink beerFemale: Attended college/community collegeAre married with kidsRide motorcycles, 4x4, ATV’sDrive Trucks or vansFish/camp/garden/sewDo craftsDrink beerGets manicures/pedicuresWears jewelry & jeans

Logo Text

Breezy Brew

Logo styles of interest
Emblem Logo
Pictorial/Combination Logo
Abstract Logo
Character Logo
Wordmark Logo
Requirements
Must have
• Eye catching & readable shelf presentation. Non-Standard art. High definition. Bold Statement. Clear design elements, various color options, High color contrast (like attached files) are needed for visual impact. Simple elements that conveys essence of the brand.
• You are designing the whole "beer can" logo elements, not just the the main logo. Things like background and side panels. Back panel for ingredients and messages to be added to. This is an "overall" can design, not just a single logo design.
• MUST HAVE THESE WORDS/SENTENCES/SECTIONS:
• Sentences: Our Breezy ales and lagers are handcrafted with some of the best ingredients the Caribbean has to offer!
• Section: So, Why Do we use can's?
• Can's eliminate potential light damage, reduce the risk of oxidation are lighter and chill quicker. Can be enjoyed on beaches and make for great recycling and table art. Plus they are the most recycled and eco-friendly material we can use. Breezy!
• BREWED AND BOTTLED/PACKED BY:
• IMPORTED BY
• ALCOHOL (ALC) ______% BY VOLUME (VOL)
• Recyclable
• GOVERNMENT WARNING:
• (1) According to the Surgeon General, women should not drink alcoholic beverages during pregnancy because of the risk of birth defects. (2) Consumption of
• alcoholic beverages impairs your ability to drive a car or operate machinery, and may cause health problems.
• Description: (This will change from beer to beer but this is good example of type language we would be using. "This Breezy Brew has a pletheria of Island goodness (there are hints of passion fruit, mango, and pineapple) along with some pleasant bitterness IPAs are known for. We can honestly say these sweet and savory flavors pair perfectly with this beer and you'll get a kick out of the IPA notes too!"
Should not have
• nudity, graphic language, skulls, flames,

```html
<!DOCTYPE html>
<html lang="en">
<head>
<meta charset="utf-8">
<title>Breezy Brew – India Pale Ale can label</title>
<link rel="stylesheet" href="https://fonts.googleapis.com/css2?family=Staatliches&family=Oswald:wght@500;700&display=swap">
<style>
  :root {
    --backdrop-light: #f7f8f8;
    --backdrop-dark: #c9cdcf;
    --teal: #2c9fa2;
    --teal-deep: #176d72;
    --teal-bright: #5fd0cf;
    --mint: #e4f4f0;
    --mint-shade: #cfe9e4;
    --brown: #4a2a16;
    --orange: #f09a1c;
    --orange-deep: #e2641a;
    --teal-text: #2b8f98;
    --ink: #3b5557;
  }
  * { box-sizing: border-box; margin: 0; padding: 0; }
  html, body { width: 1200px; height: 960px; overflow: hidden; }
  body {
    position: relative;
    background: radial-gradient(ellipse at 50% 45%, var(--backdrop-light) 0%, #eceeef 55%, var(--backdrop-dark) 100%);
    font-family: "Oswald", sans-serif;
  }
  .panel {
    position: absolute;
    top: 140px;
    width: 276px;
    height: 600px;
    overflow: hidden;
  }
  .panel--front { left: 298px; }
  .panel--back { left: 628px; }
  .band {
    position: absolute;
    left: 0; right: 0;
    background: linear-gradient(90deg, var(--teal-deep) 0%, var(--teal) 22%, var(--teal-bright) 45%, var(--teal) 70%, var(--teal-deep) 100%);
  }
  .band--top { top: 0; height: 82px; }
  .band--bottom { top: 468px; height: 132px; }
  .label {
    position: absolute;
    top: 82px; left: 0; right: 0; height: 386px;
    background: linear-gradient(90deg, var(--mint-shade) 0%, var(--mint) 30%, #f4fbf9 50%, var(--mint) 75%, var(--mint-shade) 100%);
    text-align: center;
  }
  .palm-shade {
    position: absolute;
    border-radius: 40% 40% 10% 10%;
    background: radial-gradient(ellipse at 50% 30%, rgba(160, 205, 198, 0.55), rgba(160, 205, 198, 0));
  }
  .palm-shade--left { left: -10px; top: 60px; width: 90px; height: 200px; }
  .palm-shade--right { right: -6px; top: 140px; width: 70px; height: 170px; }
  .brand-mark {
    position: absolute;
    top: 34px; left: 0; right: 0;
    display: flex; flex-direction: column; align-items: center; gap: 10px;
  }
  .brand-mark__dot {
    width: 92px; height: 92px; border-radius: 50%;
    background: var(--teal-deep);
  }
  .brand-name {
    font-family: "Staatliches", sans-serif;
    color: var(--brown);
    font-size: 46px;
    line-height: 1;
    letter-spacing: 1px;
  }
  .style-name {
    font-family: "Staatliches", sans-serif;
    font-size: 25px;
    letter-spacing: 3px;
    color: var(--orange);
    line-height: 1;
  }
  .tagline {
    font-family: "Oswald", sans-serif;
    font-weight: 700;
    font-size: 10px;
    letter-spacing: 2px;
    color: var(--teal-text);
    margin-top: 4px;
  }
  .strength {
    font-family: "Oswald", sans-serif;
    color: var(--ink);
    font-weight: 500;
    font-size: 10px;
    letter-spacing: 3px;
    display: inline-block;
  }
  .strength b {
    font-size: 19px;
    font-weight: 700;
    color: var(--teal-text);
    letter-spacing: 1px;
    margin: 0 4px;
  }
  .volume {
    display: block;
    border-top: 1px solid var(--ink);
    margin-top: 2px;
    padding-top: 1px;
    font-size: 9px;
    letter-spacing: 2.5px;
  }
  .panel--front .style-block { position: absolute; top: 284px; left: 0; right: 0; }
  .panel--front .strength-block { position: absolute; top: 336px; left: 0; right: 0; }

  .panel--back .brand-name--small {
    position: absolute; top: 22px; left: 0; right: 0;
    font-size: 32px;
  }
  .panel--back .style-block { position: absolute; top: 92px; left: 0; right: 0; }
  .panel--back .style-name { color: var(--orange-deep); font-size: 22px; }
  .description {
    position: absolute;
    top: 142px; left: 10px; right: 36px;
    font-family: "Staatliches", sans-serif;
    font-size: 11.5px;
    line-height: 16px;
    letter-spacing: 1.6px;
    color: var(--orange);
    text-align: justify;
    text-align-last: center;
  }
  .panel--back .strength-block { position: absolute; top: 336px; left: 0; right: 30px; }
  .side-copy {
    position: absolute;
    top: 14px; right: 4px;
    height: 360px;
    writing-mode: vertical-rl;
    font-family: "Staatliches", sans-serif;
    font-size: 8px;
    letter-spacing: 1px;
    line-height: 11px;
    text-align: center;
  }
  .side-copy__line { display: block; color: var(--teal-deep); }
  .side-copy__line--accent { color: var(--orange-deep); }
</style>
</head>
<body>

<section class="panel panel--front" aria-label="Front of can">
  <div class="band band--top"></div>
  <div class="label">
    <div class="palm-shade palm-shade--left" role="img" aria-label="Faint palm tree silhouette"></div>
    <div class="palm-shade palm-shade--right" role="img" aria-label="Faint palm tree silhouette"></div>
    <div class="brand-mark">
      <span class="brand-mark__dot"></span>
      <h1 class="brand-name">Breezy Brew</h1>
    </div>
    <div class="style-block">
      <h2 class="style-name">India Pale Ale</h2>
      <p class="tagline">SHORT DESCRIPTION HERE</p>
    </div>
    <div class="strength-block">
      <p class="strength">ALC<b>4.8%</b>VOL<span class="volume">12 FL.OZ / 355ML</span></p>
    </div>
  </div>
  <div class="band band--bottom"></div>
</section>

<section class="panel panel--back" aria-label="Back of can">
  <div class="band band--top"></div>
  <div class="label">
    <div class="palm-shade palm-shade--left" role="img" aria-label="Faint palm tree silhouette"></div>
    <h2 class="brand-name brand-name--small">Breezy Brew</h2>
    <div class="style-block">
      <h3 class="style-name">India Pale Ale</h3>
      <p class="tagline">SHORT DESCRIPTION HERE</p>
    </div>
    <p class="description">This Breezy Brew has a pletheria of island goodness (there are hints of passion fruit, mango, and pineapple) along with some pleasant bitterness IPAs are known for. We can honestly say these sweet and savory flavors pair perfectly with this beer and you'll get a kick out of the IPA notes too!</p>
    <div class="strength-block">
      <p class="strength">ALC<b>4.8%</b>VOL<span class="volume">12 FL.OZ / 355ML</span></p>
    </div>
    <p class="side-copy">
      <span class="side-copy__line">Our Breezy ales and lagers are handcrafted with some of the best ingredients the Caribbean has to offer!</span>
      <span class="side-copy__line side-copy__line--accent">Enjoy cold on the beach, recycle the can!</span>
    </p>
  </div>
  <div class="band band--bottom"></div>
</section>

</body>
</html>
```